■依頼目的 / 概要
電子書籍Lumora本を出版いたしますので、
表紙デザイン作成をお願いいたします。

■納品物
下記での納品をお願い致します。

JPEG形式 及び PSD形式
横1600ピクセル x 縦2560ピクセル

■本の内容

<本のタイトル>
雑貨長者の資金調達術 〜開業ローン篇〜

<サブタイトル>
会社をつくる お金を借りる 原資ができる

<キャッチコピー>
貯金してから起業なんて絶対ダメ!

<著者名>
早川蒼一

■デザイン要望
・本のタイトル / キャッチコピー / 著者名の反映をお願いします

デザインイメージ

・人物や風景の画像を背景にしていただき、
その上にタイトル等コピーを記載

・シンプルな背景にタイトル等のコピーを記載

・資産形成に関する指南書。
その第一歩である新規創業融資に
焦点を当てた内容になっていますが、
お金に関することだけではなく、
人間関係や人生設計にまで
踏み込んだ内容になっています。

・楽して稼ぐといったレベルの低いイメージをもたせるような
デザインにはしたくありません。

<表現したいイメージなど>
・高級感
・かっこいい
・信頼感

<表現したくないイメージ>
・安っぽい
・嘘くさい
・大衆的

<利用画像について>
画像素材を使用される場合には、
商用利用可の素材をお願いします。

■その他
デザインを考えるのに必要な情報が他にございましたら、
お答えしますので、遠慮なくご連絡ください。

数あるご提案の中で、もっとも世界観を表現していただいているものを当選に選ばせていただきました。

この度は、たくさんのご提案ありがとうございました。
レベルの高いご提案が多く、非常に良いデザインを得ることができました。
今回、ご縁がなかったデザイナー様。また次回、ご提案いただければ幸いです。
ありがとうございました!

```html
<!DOCTYPE html>
<html lang="ja">
<head>
<meta charset="utf-8">
<title>雑貨長者の資金調達術 〜開業ローン篇〜</title>
<link rel="stylesheet" href="https://fonts.googleapis.com/css2?family=Noto+Sans+JP:wght@700;900&family=Noto+Serif+JP:wght@500;700;900&display=swap">
<style>
  :root {
    --paper: #ffffff;
    --ink: #111111;
    --panel: #0a0a0a;
    --title: #ffffff;
    --accent: #f5e600;
    --photo-light: #f4f2ee;
    --photo-mid: #c9c3b8;
    --photo-gold: #b89a5e;
    --photo-dark: #6e6a64;
  }
  html, body { margin: 0; padding: 0; overflow: hidden; background: var(--paper); }
  .cover {
    position: relative;
    width: 750px;
    height: 1200px;
    overflow: hidden;
    background: var(--paper);
    font-family: "Noto Sans JP", sans-serif;
    color: var(--ink);
  }
  .catch-copy {
    position: absolute;
    top: 0; left: 0; width: 750px; height: 95px;
    margin: 0;
    display: flex; align-items: center; justify-content: center;
    font-size: 44px; font-weight: 700; letter-spacing: 0.01em;
    white-space: nowrap;
  }
  .title-panel {
    position: absolute;
    top: 95px; left: 0; width: 750px; height: 517px;
    background: var(--panel);
  }
  .title-line {
    position: absolute; left: 0; width: 750px;
    margin: 0; text-align: center;
    color: var(--title); font-weight: 900;
    font-size: 118px; line-height: 1; letter-spacing: -0.01em;
    white-space: nowrap;
  }
  .title-line--top { top: 50px; }
  .title-line--bottom { top: 335px; }
  .series-box {
    position: absolute;
    top: 205px; left: 125px; width: 500px; height: 82px;
    box-sizing: border-box;
    border: 5px solid var(--accent);
    display: flex; align-items: center; justify-content: center;
    color: var(--accent); font-size: 56px; font-weight: 900; letter-spacing: 0.02em;
    white-space: nowrap;
  }
  .author {
    position: absolute; top: 632px; right: 45px;
    margin: 0;
    font-family: "Noto Serif JP", serif; font-weight: 500;
    font-size: 36px; line-height: 1; letter-spacing: 0.12em;
    white-space: nowrap;
  }
  .photo {
    position: absolute; top: 700px; left: 0; width: 750px; height: 500px;
    background:
      radial-gradient(ellipse 260px 300px at 60px 430px, var(--photo-gold), transparent 70%),
      radial-gradient(ellipse 300px 260px at 720px 460px, var(--photo-dark), transparent 70%),
      radial-gradient(ellipse 240px 200px at 160px 330px, var(--photo-mid), transparent 75%),
      linear-gradient(180deg, var(--paper) 0%, var(--photo-light) 35%, var(--photo-mid) 100%);
  }
  .slogan {
    position: absolute; margin: 0;
    writing-mode: vertical-rl;
    white-space: nowrap;
    height: auto;
    font-family: "Noto Serif JP", serif; font-weight: 700;
    line-height: 1; color: var(--ink);
  }
  .slogan .big { font-size: 104px; }
  .slogan .small { font-size: 56px; }
  .slogan--borrow .big { font-size: 96px; }
  .slogan--borrow .small { font-size: 50px; }
  .slogan--company { top: 722px; left: 592px; }
  .slogan--borrow { top: 738px; left: 345px; }
  .slogan--capital { top: 748px; left: 22px; }
</style>
</head>
<body>
<main class="cover">
  <p class="catch-copy">貯金してから起業なんて絶対ダメ!</p>

  <section class="title-panel">
    <h1 class="title-line title-line--top">雑貨長者の</h1>
    <div class="series-box">開業ローン篇</div>
    <h1 class="title-line title-line--bottom">資金調達術</h1>
  </section>

  <p class="author">早川蒼一</p>

  <div class="photo" role="img" aria-label="積み上げられた硬貨の山の間を歩くビジネスマンの小さな人形の写真"></div>

  <p class="slogan slogan--company"><span class="big">会社</span><span class="small">をつくる</span></p>
  <p class="slogan slogan--borrow"><span class="big">お金</span><span class="small">を</span><span class="big">借</span><span class="small">りる</span></p>
  <p class="slogan slogan--capital"><span class="big">原資</span><span class="small">ができる</span></p>
</main>
</body>
</html>
```